Kestrel Ledger company needs ad for trade publication

Kestrel Ledgers provides sales, content, production, technology, and promotion products and services to radio stations to help increase sales and solutions to improve operations and reduce costs. We are looking for a creative ad (sizes 720x250, 300x250, 728x180) with a halloween theme. An angle could be "Nothing Scarier than starting the new year in the RED" which in business terms is a net operating loss. OR "Take a bite out of your 2024 budget". Kestrel Ledgers CAN HELP!
We want to highlight on the ad 3 key benefits that Kestrel Ledgers can help (1) "Improve your NTR" (2) "Improve your cash flow" (3) "Improve your technology and operations"
Targeting radio stations during their 2024 budgeting process

```html
<!DOCTYPE html>
<html lang="en">
<head>
<meta charset="utf-8">
<title>Kestrel Ledgers – Halloween Trade Ads</title>
<link rel="stylesheet" href="https://fonts.googleapis.com/css2?family=Black+Ops+One&family=Oswald:wght@400;500&display=swap">
<style>
  :root {
    --page: #e6e6e6;
    --ink: #0a0a0a;
    --night: #1c1c1c;
    --fog: #3a3a3a;
    --headline: #e4e4e4;
    --red: #ee1c1c;
    --white: #ffffff;
    --moon: #f2f2f2;
  }
  * { box-sizing: border-box; margin: 0; padding: 0; }
  html, body { width: 1200px; height: 680px; overflow: hidden; }
  body {
    background: radial-gradient(ellipse at center, #f4f4f4 0%, var(--page) 70%, #d4d4d4 100%);
    position: relative;
    font-family: "Oswald", sans-serif;
  }
  .ad {
    position: absolute;
    overflow: hidden;
    background: radial-gradient(ellipse at 45% 40%, var(--fog) 0%, var(--night) 45%, var(--ink) 100%);
  }
  .ad--leaderboard { left: 77px; top: 94px; width: 711px; height: 247px; }
  .ad--square { left: 814px; top: 96px; width: 291px; height: 242px; }
  .ad--banner { left: 165px; top: 367px; width: 839px; height: 208px; }

  .scene-house, .scene-moon, .scene-ground { position: absolute; }
  .scene-house {
    background:
      radial-gradient(ellipse at 55% 60%, rgba(120,10,10,.35) 0%, rgba(0,0,0,0) 45%),
      radial-gradient(ellipse at 50% 70%, #070707 0%, rgba(10,10,10,.85) 45%, rgba(10,10,10,0) 75%);
  }
  .scene-moon {
    border-radius: 50%;
    background: radial-gradient(circle at 50% 50%, var(--moon) 0%, #d2d2d2 50%, rgba(200,200,200,0) 72%);
  }
  .scene-ground {
    left: 0; right: 0;
    background: linear-gradient(180deg, rgba(0,0,0,0) 0%, #000 100%);
  }

  .headline {
    position: absolute;
    font-family: "Black Ops One", sans-serif;
    font-weight: 400;
    color: var(--headline);
    text-align: center;
    text-transform: uppercase;
    white-space: nowrap;
    transform: translateX(-50%);
  }
  .headline span { display: block; }
  .headline .hot { color: var(--red); font-style: normal; }

  .symbol {
    position: absolute;
    font-family: "Black Ops One", sans-serif;
    color: var(--red);
    line-height: 1;
  }

  .brand {
    position: absolute;
    font-family: "Oswald", sans-serif;
    font-weight: 500;
    color: var(--white);
    text-transform: uppercase;
    line-height: 1;
    white-space: nowrap;
  }
  .brand span { display: block; }
  .brand--red { color: var(--red); }

  .growth-arrow, .bar-chart { position: absolute; overflow: visible; }

  .benefits {
    position: absolute;
    display: flex;
    align-items: center;
    justify-content: center;
    color: var(--white);
    font-weight: 500;
    text-transform: uppercase;
    white-space: nowrap;
    line-height: 1;
  }
  .benefits .sep { font-weight: 400; }

  .ad--leaderboard .benefits {
    left: 0; right: 0; bottom: 0; height: 35px;
    background: var(--red);
    font-size: 16px;
    gap: 16px;
  }
  .ad--banner .benefits {
    left: 104px; width: 635px; top: 179px; height: 29px;
    background: var(--red);
    clip-path: polygon(0 0, 100% 0, 96.5% 100%, 3.5% 100%);
    font-size: 14px;
    gap: 12px;
  }
  .ad--square .benefit-list {
    position: absolute; left: 0; right: 0; top: 179px;
    color: var(--white);
    text-transform: uppercase;
    font-size: 13px;
    text-align: center;
    line-height: 1;
  }
  .benefit-list .row { display: block; white-space: nowrap; }
  .benefit-list .row + .row {
    margin-top: 7px; padding-top: 7px;
    border-top: 1px solid #3c3c3c;
    margin-left: 28px; margin-right: 28px;
  }
</style>
</head>
<body>

<section class="ad ad--leaderboard" aria-label="Leaderboard ad">
  <div class="scene-house" role="img" aria-label="Haunted house silhouette with bats and red-lit windows" style="left:10px;top:10px;width:200px;height:210px;"></div>
  <div class="scene-moon" role="img" aria-label="Full moon behind a bare tree with bats" style="left:550px;top:20px;width:160px;height:160px;"></div>
  <div class="scene-ground" role="img" aria-label="Grass silhouette along the ground" style="top:175px;height:37px;"></div>
  <svg class="bar-chart" style="left:155px;top:160px;" width="70" height="32" viewBox="0 0 70 32" aria-hidden="true">
    <rect x="0" y="20" width="7" height="12" fill="var(--red)"/>
    <rect x="11" y="12" width="7" height="20" fill="var(--red)"/>
    <rect x="22" y="4" width="7" height="28" fill="var(--red)"/>
    <rect x="33" y="14" width="7" height="18" fill="var(--red)"/>
    <rect x="44" y="22" width="7" height="10" fill="var(--red)"/>
  </svg>
  <span class="symbol" style="left:240px;top:168px;font-size:20px;">%</span>
  <span class="symbol" style="left:280px;top:176px;font-size:18px;">$</span>
  <h1 class="headline" style="left:354px;top:40px;font-size:30px;line-height:38px;">
    <span>Nothing Scarier</span>
    <span>Than Starting the New</span>
    <span>Year in the <em class="hot">Red</em></span>
  </h1>
  <svg class="growth-arrow" style="left:466px;top:112px;" width="124" height="96" viewBox="0 0 124 96" aria-hidden="true">
    <polyline points="4,92 40,58 56,70 104,22" fill="none" stroke="var(--red)" stroke-width="8"/>
    <polygon points="88,12 118,4 112,34" fill="var(--red)"/>
  </svg>
  <div class="brand" style="left:560px;top:154px;">
    <span style="font-size:30px;">Kestrel</span>
    <span style="font-size:19px;letter-spacing:1px;">Ledgers</span>
  </div>
  <div class="benefits">
    <span>Improve your NTR</span><span class="sep">|</span>
    <span>Improve your cash flow</span><span class="sep">|</span>
    <span>Improve your technology and operations</span>
  </div>
</section>

<section class="ad ad--square" aria-label="Square ad">
  <div class="scene-house" role="img" aria-label="Haunted house silhouette" style="left:5px;top:95px;width:110px;height:90px;"></div>
  <div class="scene-house" role="img" aria-label="Bare tree silhouette" style="left:200px;top:100px;width:90px;height:80px;"></div>
  <div class="scene-ground" role="img" aria-label="Grass silhouette" style="top:150px;height:26px;"></div>
  <h1 class="headline" style="left:146px;top:26px;font-size:19px;line-height:26px;">
    <span>Nothing Scarier</span>
    <span>Than Starting the</span>
    <span>New Year in the <em class="hot">Red</em></span>
  </h1>
  <div class="brand brand--red" style="left:0;right:0;top:126px;text-align:center;">
    <span style="font-size:20px;">Kestrel</span>
    <span style="font-size:12px;letter-spacing:1px;">Ledgers</span>
  </div>
  <div class="benefit-list">
    <span class="row">Improve your NTR &nbsp;|&nbsp; Improve your cash flow</span>
    <span class="row">Improve your technology and operations</span>
  </div>
</section>

<section class="ad ad--banner" aria-label="Wide banner ad">
  <div class="scene-house" role="img" aria-label="Haunted house silhouette with bats and red-lit windows" style="left:10px;top:5px;width:190px;height:175px;"></div>
  <div class="scene-moon" role="img" aria-label="Full moon behind a bare tree with bats" style="left:665px;top:10px;width:140px;height:140px;"></div>
  <div class="scene-ground" role="img" aria-label="Grass silhouette along the ground" style="top:140px;height:40px;"></div>
  <svg class="bar-chart" style="left:130px;top:135px;" width="60" height="30" viewBox="0 0 60 30" aria-hidden="true">
    <rect x="0" y="18" width="6" height="12" fill="var(--red)"/>
    <rect x="10" y="8" width="6" height="22" fill="var(--red)"/>
    <rect x="20" y="2" width="6" height="28" fill="var(--red)"/>
    <rect x="30" y="12" width="6" height="18" fill="var(--red)"/>
    <rect x="40" y="20" width="6" height="10" fill="var(--red)"/>
  </svg>
  <span class="symbol" style="left:209px;top:140px;font-size:18px;">%</span>
  <span class="symbol" style="left:570px;top:138px;font-size:18px;">$</span>
  <h1 class="headline" style="left:404px;top:32px;font-size:34px;line-height:43px;">
    <span>Nothing Scarier</span>
    <span>Than Starting the New</span>
    <span>Year in the <em class="hot">Red</em></span>
  </h1>
  <svg class="growth-arrow" style="left:596px;top:78px;" width="120" height="88" viewBox="0 0 120 88" aria-hidden="true">
    <polyline points="4,84 38,52 54,64 100,20" fill="none" stroke="var(--red)" stroke-width="7"/>
    <polygon points="86,10 114,4 108,32" fill="var(--red)"/>
  </svg>
  <div class="brand" style="left:720px;top:134px;">
    <span style="font-size:24px;">Kestrel</span>
    <span style="font-size:15px;letter-spacing:1px;">Ledgers</span>
  </div>
  <div class="benefits">
    <span>Improve your NTR</span><span class="sep">|</span>
    <span>Improve your cash flow</span><span class="sep">|</span>
    <span>Improve your technology and operations</span>
  </div>
</section>

</body>
</html>
```